Banner Designs for Drone Defense Ad Campaign

Corvane is a security consulting and services company that offers a service called SkyMindful. SkyMindful helps our customers identify security risks from drones and develops comprehensive protection programs. We are looking for a designer to create a banner ad in three sizes for our campaign.
Target Market(s)
Our campaign is geared to the sports and entertainment industry, specifically large event venues and their security operation.
Industry/Entity Type
Security
Font styles to use
Other font styles liked:
- Raleway
Requirements
Must have
- Banner Objective
The visual and textual content of the banner should prompt the viewer to quickly identify the service offered and the information that is available to download.
Banner Design
Logo: SkyMindful logo
Call to Action Button in Red: Get It Here (On Right or or Upper Right)
Title in Larger Font: Guide to UAS Risk Mitigation
Subtitle in smaller Font: 5 Steps to Develop Your Comprehensive UAS Defense Program
Background: Stadium with a drone flying in foreground
Font: Raleway
Banner Sizes
1 - 1200x670 pixels
2 - 1510x196 pixels
3 - 1200x628 pixels

```html
<!DOCTYPE html>
<html lang="en">
<head>
<meta charset="utf-8">
<title>SkyMindful – Guide to UAS Risk Mitigation</title>
<link rel="stylesheet" href="https://fonts.googleapis.com/css2?family=Raleway:wght@400;500;600&display=swap">
<style>
  :root {
    --bg: #000000;
    --title-blue: #3b7cc0;
    --text-white: #ffffff;
    --logo-grey: #d9d9d9;
    --alert-yellow: #e9d60c;
    --cta-red: #ee1c1c;
    --bracket-red: #f01414;
    --venue-tone: #1c1c1c;
    --tracker-dark: #151515;
    --tracker-green: #1f8a1a;
  }
  * { margin: 0; padding: 0; box-sizing: border-box; }
  html, body { width: 1200px; height: 156px; overflow: hidden; background: var(--bg); }
  .banner {
    position: relative;
    width: 1200px;
    height: 156px;
    background: var(--bg);
    font-family: "Raleway", Arial, sans-serif;
    overflow: hidden;
  }
  .venue-backdrop {
    position: absolute;
    left: 640px; top: 0;
    width: 400px; height: 156px;
    background: radial-gradient(ellipse at 60% 55%, var(--venue-tone) 0%, #0d0d0d 55%, var(--bg) 80%);
  }
  .brand {
    position: absolute;
    left: 20px; top: 14px;
    color: var(--logo-grey);
  }
  .brand-name { font-size: 17px; font-weight: 600; line-height: 1; }
  .brand-parent { font-size: 8px; font-weight: 600; line-height: 1; margin: 3px 0 0 38px; }
  .headline {
    position: absolute;
    left: 19px; top: 50px;
    font-size: 41px;
    font-weight: 400;
    color: var(--title-blue);
    line-height: 1;
    letter-spacing: 0.1px;
  }
  .subhead {
    position: absolute;
    left: 28px; top: 100px;
    font-size: 17.5px;
    font-weight: 500;
    color: var(--text-white);
    line-height: 1;
  }
  .tracker {
    position: absolute;
    left: 652px; top: 32px;
    width: 172px; height: 120px;
  }
  .tracker-visual {
    position: absolute;
    left: 12px; top: 12px;
    width: 150px; height: 104px;
    background: radial-gradient(ellipse at 45% 50%, var(--tracker-green) 0%, #12400f 35%, var(--tracker-dark) 70%);
  }
  .tracker-brackets { position: absolute; inset: 0; }
  .tracking-status {
    position: absolute;
    left: 838px; top: 66px;
    font-size: 13.5px;
    font-weight: 500;
    line-height: 1.22;
    color: var(--alert-yellow);
  }
  .cta-button {
    position: absolute;
    left: 994px; top: 86px;
    width: 187px; height: 53px;
    background: var(--cta-red);
    color: var(--text-white);
    font-size: 22px;
    font-weight: 500;
    display: flex;
    align-items: center;
    justify-content: center;
    text-decoration: none;
  }
</style>
</head>
<body>
  <div class="banner">
    <div class="venue-backdrop" role="img" aria-label="Faint outline of a large stadium at night"></div>

    <div class="brand">
      <div class="brand-name">SkyMindful</div>
      <div class="brand-parent">By Corvane</div>
    </div>

    <h1 class="headline">Guide to UAS Risk Mitigation</h1>
    <p class="subhead">5 Steps to Develop Your Comprehensive UAS Defense Program</p>

    <div class="tracker">
      <div class="tracker-visual" role="img" aria-label="Green silhouette of a quadcopter drone on a dark screen"></div>
      <svg class="tracker-brackets" width="172" height="120" viewBox="0 0 172 120">
        <g fill="none" stroke="var(--bracket-red)" stroke-width="5">
          <polyline points="2.5,26 2.5,2.5 26,2.5"/>
          <polyline points="146,2.5 169.5,2.5 169.5,26"/>
          <polyline points="2.5,94 2.5,117.5 26,117.5"/>
          <polyline points="146,117.5 169.5,117.5 169.5,94"/>
        </g>
      </svg>
    </div>

    <div class="tracking-status">DRONE<br>TRACKED!</div>

    <a class="cta-button" href="#">Get It Here</a>
  </div>
</body>
</html>
```